Accountant and Financial Advisor Client Presentation Folder

We are a medium sized accountancy / taxation and financial advisory firm who has just been through the process of obtaining a new logo and updating our stationary. The last piece of the puzzle is to redesign our existing client presentation folder so that it fits with our new logo (which is black and green).

We want a modern unique image, something creative, but remain professional. Also portray integrity and look approachable. We want to appeal to the younger generation while not losing the respect of our more conservative older clients.

The necessary words and logo to be included on the folder are attached (Presentation Folder Brief), the overall design of the folder is up to you.
We want our new folder to look attractive and stand out from the crowd preferably with a graphic. We have included our old folder which we like (has the dandelion) however the colours etc have now changed as per the black and green mock-up folder example.
We would like a redesign so that we have a graphic to break up the colour. We are open to design changes on the shape of the folder.

Target Market(s)

younger generation while not losing the respect of our more conservative older clients

Industry/Entity Type

Financial

Requirements
Must have
• Graphic in the folder Design

```html
<!DOCTYPE html>
<html lang="en">
<head>
<meta charset="utf-8">
<title>Lumen Ledger – Presentation Folder</title>
<link href="https://fonts.googleapis.com/css2?family=Montserrat:wght@500;600&family=Open+Sans:wght@400;600;700&display=swap" rel="stylesheet">
<style>
  :root {
    --green: #45ff10;
    --green-light: #b8ff3a;
    --green-deep: #2fe20c;
    --accent: #a6e22a;
    --charcoal: #151819;
    --white: #ffffff;
    --slate: #5b5fb8;
    --fold: rgba(255,255,255,0.7);
    --canvas: #ffffff;
  }
  html, body { margin: 0; padding: 0; overflow: hidden; background: var(--canvas); }
  .folder {
    position: relative; width: 1200px; height: 822px; overflow: hidden;
    background: var(--canvas); font-family: "Open Sans", sans-serif;
  }
  .panel { position: absolute; }
  .panel--back, .panel--front {
    background:
      radial-gradient(ellipse at 20% 5%, var(--green-light) 0%, transparent 30%),
      radial-gradient(ellipse at 48% 45%, var(--green-light) 0%, transparent 35%),
      radial-gradient(ellipse at 95% 40%, #c4ff4a 0%, transparent 28%),
      radial-gradient(ellipse at 70% 2%, #d6ff6a 0%, transparent 22%),
      linear-gradient(160deg, var(--green) 0%, var(--green-deep) 60%, var(--green) 100%);
  }
  .panel--back { left: 0; top: 0; width: 444px; height: 614px; }
  .panel--front { left: 444px; top: 0; width: 434px; height: 604px; }
  .folds { position: absolute; left: 0; top: 0; }

  .headline {
    position: absolute; left: 490px; top: 206px; margin: 0;
    font-family: "Montserrat", sans-serif; font-weight: 600;
    font-size: 25px; line-height: 22.6px; color: var(--white);
    letter-spacing: 0.2px;
  }
  .services {
    position: absolute; left: 466px; top: 562px; width: 390px;
    font-family: "Open Sans", sans-serif; font-size: 9.4px; color: var(--white);
    letter-spacing: 0.3px; white-space: nowrap;
  }
  .services span { margin: 0 5px; }
  .about {
    position: absolute; left: 210px; top: 443px; width: 211px; margin: 0;
    font-size: 7.6px; line-height: 12px; text-align: right; color: var(--white);
  }
  .about strong { font-weight: 700; }
  .about .about__name { color: var(--slate); font-weight: 700; }

  .flap-shape { position: absolute; left: 0; top: 0; }
  .brand {
    position: absolute; left: 914px; top: 212px; width: 240px;
  }
  .brand__name {
    display: flex; align-items: center; gap: 8px;
    font-family: "Montserrat", sans-serif; font-weight: 600; font-size: 20px;
    color: var(--accent); letter-spacing: 0.5px;
  }
  .brand__mark { width: 12px; height: 12px; background: var(--accent); }
  .brand__tagline {
    margin-top: 10px; font-family: "Montserrat", sans-serif; font-weight: 600;
    font-size: 5px; color: var(--white); letter-spacing: 0.2px;
  }
  .firm-type {
    position: absolute; left: 916px; top: 318px; margin: 0;
    font-size: 9.2px; line-height: 11px; color: var(--white);
  }
  .contact {
    position: absolute; left: 916px; top: 512px; margin: 0;
    font-size: 5.6px; line-height: 8.2px; color: var(--white); font-style: normal;
  }
  .contact b { color: var(--accent); font-weight: 600; }
  .web {
    position: absolute; left: 916px; top: 563px; margin: 0;
    font-size: 8.4px; font-weight: 600; color: var(--accent);
  }

  .panel--pocket { left: 435px; top: 604px; width: 453px; height: 218px; background: var(--charcoal); }
  .pocket-services {
    position: absolute; left: 690px; top: 625px; width: 160px; margin: 0;
    transform: rotate(180deg); transform-origin: center;
    font-size: 8.6px; line-height: 13px; color: var(--white); letter-spacing: 0.3px;
    text-align: left;
  }
</style>
</head>
<body>
<div class="folder">
  <div class="panel panel--back" role="img" aria-label="Faceted green geometric background graphic"></div>
  <div class="panel panel--front" role="img" aria-label="Faceted green geometric background graphic"></div>
  <div class="panel panel--pocket"></div>

  <svg class="flap-shape" width="1200" height="822" aria-hidden="true">
    <polygon points="878,10 916,10 1200,238 1072,604 878,604" fill="var(--charcoal)"/>
  </svg>

  <svg class="folds" width="1200" height="822" aria-hidden="true">
    <rect x="8" y="8" width="874" height="592" fill="none" stroke="var(--fold)" stroke-width="0.6" stroke-dasharray="3 2" opacity="0.5"/>
    <line x1="444" y1="0" x2="444" y2="604" stroke="var(--fold)" stroke-width="0.8"/>
    <polyline points="404,10 124,238 250,604" fill="none" stroke="var(--fold)" stroke-width="0.8"/>
    <line x1="292" y1="198" x2="292" y2="360" stroke="var(--fold)" stroke-width="0.6" stroke-dasharray="3 2"/>
    <line x1="444" y1="610" x2="444" y2="812" stroke="#888" stroke-width="0.6" stroke-dasharray="3 2"/>
    <line x1="878" y1="606" x2="878" y2="688" stroke="#888" stroke-width="0.6" stroke-dasharray="3 2"/>
    <line x1="444" y1="812" x2="878" y2="688" stroke="#888" stroke-width="0.6" stroke-dasharray="3 2"/>
    <rect x="482" y="626" width="170" height="104" fill="none" stroke="#888" stroke-width="0.6" stroke-dasharray="3 2"/>
    <line x1="477" y1="642" x2="497" y2="622" stroke="#aaa" stroke-width="0.6"/>
    <line x1="638" y1="735" x2="658" y2="715" stroke="#aaa" stroke-width="0.6"/>
  </svg>

  <h1 class="headline">BUILD<br>YOUR<br>BUSINESS &amp;<br>GROW<br>YOUR<br>WEALTH</h1>
  <div class="services">ACCOUNTING<span>I</span>TAX AGENTS<span>I</span>FINANCIAL ADVICE<span>I</span>SELF MANAGED SUPER FUNDS</div>

  <p class="about"><span class="about__name">Lumen Ledger</span> is a results-focused <strong>CPA Accounting, Taxation and Financial Advisory firm</strong> that integrates your personal, business and financial needs in the interests of better outcomes for you. We see ourselves as a professional advisor for life, able to deliver complete <strong>financial solutions</strong> that considers <strong>tax, business, superannuation, retirement</strong> and <strong>investment planning</strong> proactively.</p>

  <div class="brand">
    <div class="brand__name"><span class="brand__mark"></span>LUMEN LEDGER</div>
    <div class="brand__tagline">BUILD YOUR BUSINESS &amp; GROW YOUR WEALTH</div>
  </div>
  <p class="firm-type">CPA Accounting, Taxation and<br>Financial Advisory Firm</p>
  <address class="contact">Suite 8 / 41 Harbour View Road<br>PO Box 1180, Kareela NSW 2232<br><b>P</b> : (02) 5550 1234<br><b>E</b> : hello@lumenledger.com.au</address>
  <p class="web">www.lumenledger.com.au</p>

  <p class="pocket-services">ACCOUNTING<br>TAX AGENTS<br>FINANCIAL ADVICE<br>SELF MANAGED SUPER FUNDS</p>
</div>
</body>
</html>
```